National Intensive Course Provider needs an advert designed to appear in trams

We need an advertisement designed to put in trams, the dimensions are 660mm wide and 203mm height. We offer intensive driving courses all over the UK, allowing pupils to complete a full driving course within a week/two weeks with both the theory and practical tests included in the course (as required). We would like the colours used to be green and dark blue, maybe red also, whatever looks best from them colours really.

Key Points to highlight:
- Pass your driving test within 1 week
- Start your course as early as next week
- Both tests included as part of your course (if required)

I have attached some images which could be included in the design

```html
<!DOCTYPE html>
<html lang="en">
<head>
<meta charset="utf-8">
<title>Route One Driving – Tram Advert</title>
<link rel="stylesheet" href="https://fonts.googleapis.com/css2?family=Roboto+Condensed:wght@700&family=Open+Sans:wdth,wght@75..100,700&display=swap">
<style>
  :root {
    --page: #ffffff;
    --blue: #1c3e9e;
    --blue-deep: #0f2466;
    --navy: #0b0d4a;
    --red: #f20000;
    --red-border: #e8141e;
    --white: #ffffff;
    --leaf: #5e7f3c;
    --leaf-light: #9bb56a;
    --car: #c8161e;
  }
  html, body {
    margin: 0;
    padding: 0;
    overflow: hidden;
    background: var(--page);
  }
  .advert {
    position: relative;
    width: 1200px;
    height: 391px;
    background: var(--page);
    overflow: hidden;
    font-family: "Roboto Condensed", "Arial Narrow", sans-serif;
    color: var(--white);
  }
  .advert__shapes {
    position: absolute;
    inset: 0;
  }
  .brand-panel {
    position: absolute;
    left: 60px;
    top: 80px;
    width: 276px;
    height: 186px;
    box-sizing: border-box;
    background: var(--navy);
    border: 2px solid var(--red-border);
    border-radius: 34px;
    display: flex;
    flex-direction: column;
    align-items: center;
    justify-content: center;
    gap: 6px;
    box-shadow: 0 2px 6px rgba(0,0,0,0.35);
  }
  .brand-panel__name {
    margin: 0;
    font-size: 46px;
    font-weight: 700;
    line-height: 1;
    letter-spacing: 1px;
    text-transform: uppercase;
  }
  .brand-panel__tagline {
    margin: 0;
    font-size: 46px;
    font-weight: 700;
    line-height: 1;
    letter-spacing: 1px;
    text-transform: uppercase;
  }
  .phone {
    position: absolute;
    left: 50px;
    top: 296px;
    width: 310px;
    margin: 0;
    text-align: center;
    font-size: 50px;
    font-weight: 700;
    line-height: 1;
  }
  .headline {
    position: absolute;
    right: 56px;
    top: 30px;
    margin: 0;
    text-align: right;
    font-size: 80px;
    font-weight: 700;
    line-height: 74px;
    letter-spacing: -0.5px;
    text-shadow: 2px 3px 4px rgba(0,0,0,0.35);
  }
  .tests-note {
    position: absolute;
    right: 56px;
    top: 203px;
    margin: 0;
    font-family: "Open Sans", "Arial Narrow", sans-serif;
    font-stretch: 75%;
    font-weight: 700;
    font-size: 24px;
    line-height: 1;
    white-space: nowrap;
  }
  .start-offer {
    position: absolute;
    right: 56px;
    top: 258px;
    margin: 0;
    text-align: right;
    font-size: 46px;
    font-weight: 700;
    line-height: 48px;
  }
  .start-offer__lead {
    display: block;
    text-transform: uppercase;
    font-size: 48px;
  }
</style>
</head>
<body>
<main class="advert">
  <svg class="advert__shapes" width="1200" height="391" viewBox="0 0 1200 391">
    <defs>
      <linearGradient id="blueFade" x1="0" y1="0" x2="0" y2="1">
        <stop offset="0" stop-color="#142f82"/>
        <stop offset="0.5" stop-color="#2448b0"/>
        <stop offset="1" stop-color="#13307f"/>
      </linearGradient>
      <pattern id="streaks" width="400" height="6" patternUnits="userSpaceOnUse">
        <rect x="0" y="0" width="260" height="1.5" fill="#ffffff" opacity="0.06"/>
        <rect x="120" y="3" width="220" height="1" fill="#000000" opacity="0.08"/>
      </pattern>
      <linearGradient id="photoTones" x1="0" y1="0" x2="1" y2="1">
        <stop offset="0" stop-color="#9bb56a"/>
        <stop offset="0.45" stop-color="#5e7f3c"/>
        <stop offset="1" stop-color="#c8161e"/>
      </linearGradient>
    </defs>
    <rect class="blue-field" x="18" y="18" width="1164" height="356" fill="url(#blueFade)"/>
    <rect class="blue-streaks" x="18" y="18" width="1164" height="356" fill="url(#streaks)"/>
    <g role="img" aria-label="Photo of a smiling pupil holding a driving test pass certificate beside a red car">
      <polygon class="photo-area" points="400,240 662,240 662,374 472,374" fill="url(#photoTones)"/>
    </g>
    <rect class="offer-band" x="662" y="240" width="520" height="134" fill="var(--navy)"/>
    <polygon class="headline-arrow" points="484,18 1182,18 1182,240 400,240 364,188"
             fill="var(--red)" stroke="var(--white)" stroke-width="4" stroke-linejoin="round"/>
    <rect x="1182" y="16" width="4" height="230" fill="var(--page)"/>
    <rect x="480" y="14" width="706" height="4" fill="var(--page)"/>
  </svg>

  <div class="brand-panel">
    <p class="brand-panel__name">Route One</p>
    <p class="brand-panel__tagline">Driving</p>
  </div>

  <p class="phone">000 000 0000</p>

  <h1 class="headline">Pass Your Driving<br>Test Within 1 Week</h1>

  <p class="tests-note">Theory and practical tests included as part of your course (if required)</p>

  <p class="start-offer">
    <span class="start-offer__lead">Start your course</span>
    as early as Next Week
  </p>
</main>
</body>
</html>
```